label design for soy candle

I am a start up making soy candles and other products involving scents.
On the label should be in writing : Wild Fern, Handgemacht in der Schweiz, Sojakerze, my logo with the name Pertwick Candles on it. I will upload the currant label of my candles, but I want something more fashioned. The color of the label should be black with Wild Fern written in gold, and the rest in white. Or maybe suggest something different, I am open to new designs. I am also open to change the logo, except the flower has to stay.
Sizes : square 60x60mm / round 50mm / rectangle 70x20mm ( for different jars )

```html
<!DOCTYPE html>
<html lang="de">
<head>
<meta charset="UTF-8">
<title>Pertwick Candles – Wild Fern label</title>
<link href="https://fonts.googleapis.com/css2?family=Amatic+SC:wght@700&family=Tinos:wght@400;700&display=swap" rel="stylesheet">
<style>
  :root {
    --page: #ffffff;
    --label-black: #0b0b0b;
    --gold: #c9a27e;
    --white: #ffffff;
  }
  html, body {
    margin: 0;
    padding: 0;
    width: 1200px;
    height: 1200px;
    overflow: hidden;
    background: var(--page);
  }
  .canvas {
    position: relative;
    width: 1200px;
    height: 1200px;
  }
  .label {
    position: absolute;
    left: 150px;
    top: 150px;
    width: 900px;
    height: 900px;
    background: var(--label-black);
  }
  .label-frame {
    position: absolute;
    inset: 0;
  }
  .brand-name {
    position: absolute;
    top: 128px;
    left: 0;
    width: 100%;
    text-align: center;
    font-family: "Tinos", "Times New Roman", serif;
    font-weight: 700;
    font-size: 26px;
    line-height: 1;
    letter-spacing: 4px;
    color: var(--white);
    margin: 0;
  }
  .scent-name {
    position: absolute;
    top: 378px;
    left: 0;
    width: 100%;
    text-align: center;
    font-family: "Amatic SC", "Arial Narrow", sans-serif;
    font-weight: 700;
    font-size: 150px;
    line-height: 1;
    letter-spacing: 8px;
    color: var(--gold);
    margin: 0;
  }
  .scent-divider {
    position: absolute;
    top: 508px;
    left: 240px;
    width: 420px;
    height: 30px;
  }
  .product-type {
    position: absolute;
    top: 688px;
    left: 0;
    width: 100%;
    text-align: center;
    font-family: "Tinos", "Times New Roman", serif;
    font-size: 44px;
    line-height: 1;
    color: var(--white);
    margin: 0;
  }
  .product-type .dots {
    display: inline-block;
    font-size: 22px;
    letter-spacing: 10px;
    vertical-align: middle;
    margin: 0 6px;
  }
  .origin {
    position: absolute;
    top: 762px;
    left: 0;
    width: 100%;
    text-align: center;
    font-family: "Tinos", "Times New Roman", serif;
    font-size: 48px;
    line-height: 1;
    color: var(--white);
    margin: 0;
  }
</style>
</head>
<body>
<main class="canvas">
  <section class="label">
    <svg class="label-frame" width="900" height="900" viewBox="0 0 900 900">
      <g stroke="var(--gold)" stroke-width="2">
        <line x1="80" y1="50" x2="820" y2="50"/>
        <line x1="80" y1="850" x2="820" y2="850"/>
        <line x1="50" y1="80" x2="50" y2="820"/>
        <line x1="850" y1="80" x2="850" y2="820"/>
      </g>
      <g fill="var(--gold)">
        <rect role="img" aria-label="corner star ornament" x="43" y="43" width="14" height="14"/>
        <rect role="img" aria-label="corner star ornament" x="843" y="43" width="14" height="14"/>
        <rect role="img" aria-label="corner star ornament" x="43" y="843" width="14" height="14"/>
        <rect role="img" aria-label="corner star ornament" x="843" y="843" width="14" height="14"/>
      </g>
    </svg>

    <p class="brand-name">PERTWICK CANDLES</p>

    <h1 class="scent-name">WILD FERN</h1>

    <svg class="scent-divider" width="420" height="30" viewBox="0 0 420 30">
      <line x1="0" y1="15" x2="160" y2="15" stroke="var(--gold)" stroke-width="2"/>
      <line x1="260" y1="15" x2="420" y2="15" stroke="var(--gold)" stroke-width="2"/>
      <rect role="img" aria-label="small dotted ornament" x="168" y="9" width="84" height="12" fill="var(--gold)"/>
    </svg>

    <p class="product-type"><span class="dots">•••</span>Sojakerze<span class="dots">•••</span></p>
    <p class="origin">Handgemacht in der Schweiz</p>
  </section>
</main>
</body>
</html>
```